Online-Marketing Material für Immobilienmakler
Zielgruppe
Ich bin Immobilienmakler und beschäftige mich mit der Vermietung / Verkauf von Immobilien. Zielgruppe sind Käufer / Verkäufer bzw. Vermieter und Mieter
Aufgabenstellung
Das Design soll sich am bestehenden CI orientieren, gleichzeitig modern gestaltet werden. Hierbei geht es mir um die Erstellung von Desginvorlagen für Post in Social-Media-Kanälen, welche ich je nach Inhalt entsprechend anpassen kann.
Inbesondere soll es eine Vorlage für die Vorstellung von neuen Objekten geben, welche immer wieder genutzt werden kann und daher die Inhalte in Canva anpassbar sind.

```html
<!DOCTYPE html>
<html lang="de">
<head>
<meta charset="utf-8">
<title>Objektvorstellung – klarhaus</title>
<link href="https://fonts.googleapis.com/css2?family=Red+Hat+Display:wght@400;500;700;800&display=swap" rel="stylesheet">
<style>
  :root {
    --green: #7cbd42;
    --blue: #0882c4;
    --blue-deep: #0e6aa3;
    --slate: #51565f;
    --white: #ffffff;
    --backdrop: #6b6b6b;
    --photo-sky: #9fb8c9;
    --photo-hill: #3f6b3a;
    --photo-house: #d9dcdf;
  }
  * { margin: 0; padding: 0; box-sizing: border-box; }
  html, body {
    width: 1200px; height: 1117px; overflow: hidden;
    background: var(--backdrop);
    font-family: "Red Hat Display", sans-serif;
  }
  .post {
    position: absolute; left: 61px; top: 20px;
    width: 1077px; height: 1077px;
    background: var(--white);
  }
  .post__frame {
    position: absolute; left: 28px; top: 28px;
    width: 1021px; height: 1021px;
    border: 2px solid var(--green);
    border-bottom: none;
  }
  .brand {
    position: absolute; left: 28px; top: 28px; width: 1021px; height: 167px;
    display: flex; align-items: center; justify-content: center; gap: 16px;
  }
  .brand__mark { width: 46px; height: 46px; background: var(--green); }
  .brand__name {
    font-size: 62px; font-weight: 700; color: var(--blue); letter-spacing: -1px;
  }
  .feature {
    position: absolute; left: 28px; top: 195px; width: 1021px; height: 343px;
    display: flex;
  }
  .feature__photo {
    width: 634px; height: 100%;
    background: linear-gradient(180deg, var(--photo-sky) 0%, var(--photo-hill) 30%, var(--photo-house) 55%, #b9b4ae 100%);
  }
  .feature__headline {
    flex: 1; background: var(--green); color: var(--white);
    padding: 26px 46px 0 20px;
    font-size: 38px; font-weight: 800; line-height: 41px;
    text-align: right; text-transform: uppercase; letter-spacing: -0.3px;
  }
  .tagline {
    position: absolute; left: 28px; top: 538px; width: 1021px; height: 90px;
    background: var(--slate); color: var(--white);
    display: flex; align-items: center; justify-content: center;
    font-size: 33px; font-weight: 500; letter-spacing: 0.2px;
  }
  .benefits {
    position: absolute; left: 28px; top: 628px; width: 1021px; height: 327px;
    background: var(--blue);
  }
  .benefits__track { position: absolute; left: 0; top: 0; }
  .benefit__text {
    position: absolute; top: 144px; width: 260px;
    color: var(--white); font-size: 22px; line-height: 27px;
    text-align: center;
  }
  .contact {
    position: absolute; left: 28px; top: 955px; width: 1021px; height: 92px;
    background: var(--green); color: var(--white);
    display: flex; align-items: center; justify-content: center;
    font-size: 21px; font-weight: 500;
  }
  .contact__item { display: flex; align-items: center; gap: 12px; padding: 0 13px; }
  .contact__item + .contact__item { border-left: 1px solid rgba(255,255,255,0.5); }
  .contact__icon { width: 26px; height: 26px; }
</style>
</head>
<body>
  <main class="post">
    <div class="post__frame"></div>

    <header class="brand">
      <span class="brand__mark"></span>
      <span class="brand__name">klarhaus</span>
    </header>

    <section class="feature">
      <div class="feature__photo" role="img" aria-label="Foto eines weißen Einfamilienhauses mit rotem Ziegeldach, Garage und Carport vor bewaldeten Hügeln"></div>
      <h1 class="feature__headline">Das<br>“Hier kann<br>ich schnell<br>einziehen”<br>Haus in toller<br>Lage von<br>Detting</h1>
    </section>

    <div class="tagline">KOMPETENT. ZUVERLÄSSIG. FAIR.</div>

    <section class="benefits">
      <svg class="benefits__track" width="1021" height="140" viewBox="0 0 1021 140" aria-hidden="true">
        <line x1="172" y1="78" x2="848" y2="78" stroke="var(--blue-deep)" stroke-width="4"/>
        <g id="tick">
          <circle cx="172" cy="78" r="47" fill="var(--blue-deep)"/>
          <circle cx="172" cy="78" r="38" fill="var(--green)"/>
          <path d="M155 78 l12 12 l22 -22" fill="none" stroke="var(--blue-deep)" stroke-width="8" stroke-linecap="square"/>
        </g>
        <use href="#tick" x="338"/>
        <use href="#tick" x="676"/>
      </svg>
      <p class="benefit__text" style="left:42px">Lorem ipsum dolor sit amet, consectetuer adipiscing elit, sed nonummy nibh euis tincidunt ut laoreet.</p>
      <p class="benefit__text" style="left:380px">Lorem ipsum dolor sit amet, consectetuer adipiscing elit, sed nonummy nibh euis tincidunt ut laoreet.</p>
      <p class="benefit__text" style="left:718px">Lorem ipsum dolor sit amet, consectetuer adipiscing elit, sed nonummy nibh euis tincidunt ut laoreet.</p>
    </section>

    <footer class="contact">
      <span class="contact__item">
        <svg class="contact__icon" viewBox="0 0 26 26" aria-hidden="true"><circle cx="13" cy="13" r="13" fill="#fff"/><path d="M9 7 l3 3 -2 2 c1 2 2 3 4 4 l2 -2 3 3 -2 2 c-5 0 -10 -5 -10 -10z" fill="var(--green)"/></svg>
        0 7000 / 123 4560
      </span>
      <span class="contact__item">
        <svg class="contact__icon" viewBox="0 0 26 26" aria-hidden="true"><rect x="2" y="6" width="22" height="15" fill="none" stroke="#fff" stroke-width="2"/><path d="M2 6 l11 9 11 -9 M2 21 l8 -7 M24 21 l-8 -7" fill="none" stroke="#fff" stroke-width="2"/></svg>
        info@klarhaus-makler.de
      </span>
      <span class="contact__item">
        <svg class="contact__icon" viewBox="0 0 26 26" aria-hidden="true"><g fill="none" stroke="#fff" stroke-width="1.8"><circle cx="13" cy="13" r="11"/><ellipse cx="13" cy="13" rx="5" ry="11"/><path d="M2 13 h22 M4 7 h18 M4 19 h18"/></g></svg>
        www.klarhaus-makler.de
      </span>
    </footer>
  </main>
</body>
</html>
```